Postcard Design

I am attempting to put together a post card that meats the KVT requirements for there mail pay zip code mail program. They are tell different requirements depending on who you talk too. Graniton Parcel office, hhhmmmm shock.
I want a post card that looks good and advertises free listings. I need to make sure that this card says in small print that "certain conditions may apply". I want the card to have to be presented in order to get this deal. That this deal is for a limited time only. The companies address is 27310 E Harlow Ave, Ste 118B, Southfield, MI 48391. The office number is 248-555-0143.
Target Market(s)
I am attempting to market to homeowners that want to list there property for sale on the MLS
Industry/Entity Type
Office
Look and feel

```html
<!DOCTYPE html>
<html lang="en">
<head>
<meta charset="utf-8">
<title>Harborline Real Estate — Free Listing Postcard</title>
<link rel="stylesheet" href="https://fonts.googleapis.com/css2?family=Source+Sans+3:wght@400;600&display=swap">
<style>
  :root {
    --stage: #1c1c1c;
    --paper: #ffffff;
    --paper-shade: #eef0f3;
    --navy: #2a2f7a;
    --navy-deep: #1f2466;
    --navy-soft: #5a5fa8;
    --panel-grey: #c9cacc;
    --ink: #333333;
    --stamp-line: #9a9a9a;
  }
  * { box-sizing: border-box; margin: 0; padding: 0; }
  html, body {
    width: 1200px; height: 1200px; overflow: hidden;
    background: var(--stage);
    font-family: "Source Sans 3", "Myriad Pro", Arial, sans-serif;
  }
  .canvas { position: relative; width: 1200px; height: 1200px; }

  .postcard {
    position: absolute;
    background: linear-gradient(160deg, var(--paper) 55%, var(--paper-shade) 100%);
    box-shadow: 0 4px 14px rgba(0,0,0,.45);
  }
  .postcard--back  { left: 419px; top: 26px;  width: 727px; height: 558px; }
  .postcard--front { left: 65px;  top: 612px; width: 727px; height: 564px; }

  .photo { position: absolute; }
  .photo--feature {
    left: 11px; top: 10px; width: 340px; height: 289px; border-radius: 16px;
    background: linear-gradient(180deg, #2f5fb8 0%, #9fb3c9 38%, #b9a27c 55%, #3b4a2e 72%, #151d12 100%);
  }
  .offer-panel {
    position: absolute; left: 11px; top: 308px; width: 340px; height: 156px;
    border-radius: 14px; color: #fff; text-align: center;
    background: linear-gradient(180deg, var(--navy-soft) 0%, var(--navy) 60%, var(--navy-deep) 100%);
    padding-top: 12px;
  }
  .offer-panel .deal { font-size: 25px; line-height: 31px; }
  .offer-panel .call { font-size: 19px; margin-top: 8px; }
  .offer-panel .phone { font-size: 29px; margin-top: 2px; }

  .return-address { position: absolute; left: 364px; top: 42px; color: var(--ink); }
  .return-address .company { color: var(--navy); font-size: 14px; font-weight: 600; margin-bottom: 6px; }
  .return-address p { font-size: 13px; line-height: 18px; }

  .stamp-box {
    position: absolute; left: 551px; top: 10px; width: 166px; height: 166px;
    border: 1px solid var(--stamp-line); background: #fff;
  }

  .photo--house-a { left: 10px;  top: 13px;  width: 222px; height: 155px; border-top-left-radius: 14px;
    background: linear-gradient(180deg, #3d6ec0 0%, #a9b8c8 45%, #d7d3c8 60%, #5d7040 85%, #3a4a2a 100%); }
  .photo--house-b { left: 10px;  top: 176px; width: 222px; height: 160px;
    background: linear-gradient(180deg, #4f7fcf 0%, #b8c9dc 40%, #a79a88 58%, #4f8a2e 78%, #2f5a1d 100%); }
  .photo--house-c { left: 496px; top: 13px;  width: 222px; height: 155px; border-top-right-radius: 14px;
    background: linear-gradient(180deg, #244fa6 0%, #5b7fc4 40%, #cfd3d8 58%, #2f5a22 75%, #3c7a2a 100%); }
  .photo--house-d { left: 496px; top: 176px; width: 222px; height: 160px;
    background: linear-gradient(180deg, #9fb4cc 0%, #c8cfd6 30%, #d9d2b4 55%, #6f6f5c 80%, #4a4a3a 100%); }

  .headline-panel {
    position: absolute; left: 240px; top: 13px; width: 248px; height: 92px;
    background: var(--navy); color: #fff; display: flex; align-items: center; justify-content: center;
  }
  .headline-panel h1 { font-weight: 400; font-size: 43px; letter-spacing: .3px; }

  .info-panel {
    position: absolute; left: 240px; top: 115px; width: 248px; height: 221px;
    background: var(--panel-grey); color: var(--navy); text-align: center; padding-top: 12px;
  }
  .info-panel .pitch { font-size: 20px; line-height: 25px; }
  .info-panel .call { font-size: 20px; margin-top: 20px; }
  .info-panel .phone { font-size: 29px; margin-top: 2px; }
  .info-panel .fine-print { font-size: 13px; margin-top: 22px; }

  .rule { position: absolute; left: 10px; width: 708px; background: var(--navy); }
  .rule--upper { top: 222px; }
  .rule--top-thick { top: 344px; height: 3px; }
  .rule--top-thin  { top: 350px; height: 1px; }
  .rule--bottom-thin { top: 525px; height: 1px; }
  .footer-band {
    position: absolute; left: 10px; top: 529px; width: 708px; height: 22px;
    border-radius: 0 0 12px 12px;
    background: linear-gradient(90deg, var(--navy-deep) 0%, var(--navy) 50%, var(--navy-soft) 100%);
  }
  .brand-name {
    position: absolute; left: 0; top: 430px; width: 727px; text-align: center;
    color: var(--navy); font-size: 43px; font-weight: 400; letter-spacing: .3px;
  }
</style>
</head>
<body>
<div class="canvas">

  <section class="postcard postcard--back" aria-label="Postcard address side">
    <div class="photo photo--feature" role="img" aria-label="Photo of a two-storey suburban house at dusk with a landscaped front yard"></div>
    <div class="offer-panel">
      <p class="deal">This deal is<br>for a limited time only.</p>
      <p class="call">Call Us Today!</p>
      <p class="phone">248-555-0143</p>
    </div>
    <div class="return-address">
      <p class="company">Harborline Real Estate, Inc.</p>
      <p>27310 E Harlow Ave.</p>
      <p>Ste 118B, Southfield</p>
      <p>MI 48391</p>
    </div>
    <div class="stamp-box" aria-label="Stamp area"></div>
  </section>

  <section class="postcard postcard--front" aria-label="Postcard front">
    <div class="photo photo--house-a" role="img" aria-label="Photo of a large white house with a driveway"></div>
    <div class="photo photo--house-b" role="img" aria-label="Photo of a stone house with a green lawn"></div>
    <div class="headline-panel"><h1>Free Listing</h1></div>
    <div class="info-panel">
      <p class="pitch">Let your<br>property to be listed.</p>
      <p class="call">Call Us Today!</p>
      <p class="phone">248-555-0143</p>
      <p class="fine-print">Certain conditions may apply.</p>
    </div>
    <div class="photo photo--house-c" role="img" aria-label="Photo of a gabled house behind a hedge under blue sky"></div>
    <div class="photo photo--house-d" role="img" aria-label="Photo of a two-storey house with a garage"></div>
    <div class="rule rule--top-thick"></div>
    <div class="rule rule--top-thin"></div>
    <p class="brand-name">Harborline Real Estate, Inc.</p>
    <div class="rule rule--bottom-thin"></div>
    <div class="footer-band"></div>
  </section>

</div>
</body>
</html>
```